Waterproofing Construction company needs letterhead

I need a letterhead design for a commercial waterproofing construction company. We would like to see designs that are contemporary, clean, sleek and use our logo. Our current design is dated. I would also like a cover page (see example) that goes with our letterhead. I would like for the footer to have our address, website, and phone number

Target Market(s)

Customers, potential customers.

Font styles to use
Sans Serif

Requirements
Must have
• logo, website, address, phone numbers, only our colors, tahoma font
• PMS: 295C PMS: 2995C
• CMYK: 100/84/36/39 CMYK: 80/12/1/0
• RGB: 16/44/82 RGB: 0/167/224
• HEX#: #102C52 HEX#: #00A7E0
• Black & White: 100% Black & White: 32%
• Gray Scale: 90% Gray Scale: 32%
Nice to have
• Our "icon" logo attached would be nice somewhere on the page.

```html
<!DOCTYPE html>
<html lang="en">
<head>
<meta charset="utf-8">
<title>Korven Waterproofing Letterhead</title>
<link href="https://fonts.googleapis.com/css2?family=Questrial&family=Roboto:wght@400;700&display=swap" rel="stylesheet">
<style>
  :root {
    --navy: #102C52;
    --cyan: #00A7E0;
    --backdrop: #e6e7e9;
    --body-text: #5a5a5c;
    --heading-text: #4a4a4c;
    --footer-text: #444446;
    --signature-tone: #c9d6ee;
  }
  * { margin: 0; padding: 0; box-sizing: border-box; }
  html, body {
    width: 1024px;
    height: 1200px;
    overflow: hidden;
    background: var(--backdrop);
  }
  .letterhead {
    position: absolute;
    left: 112px;
    top: 50px;
    width: 800px;
    height: 1100px;
    background: linear-gradient(100deg, #f7f7f8 0%, #efeff0 60%, #e9e9ea 100%);
    box-shadow: 0 6px 24px rgba(0,0,0,0.12);
    overflow: hidden;
  }
  .brand-name {
    position: absolute;
    top: 88px;
    left: 0;
    width: 100%;
    text-align: center;
    font-family: "Roboto", sans-serif;
    font-weight: 700;
    font-size: 58px;
    letter-spacing: 1px;
    color: var(--navy);
    line-height: 1;
  }
  .salutation {
    position: absolute;
    top: 292px;
    left: 77px;
    font-family: "Questrial", sans-serif;
    font-size: 19px;
    color: var(--heading-text);
  }
  .letter-body {
    position: absolute;
    top: 349px;
    left: 77px;
    right: 66px;
    font-family: "Questrial", sans-serif;
    font-size: 12.1px;
    line-height: 14.4px;
    color: var(--body-text);
    text-align: justify;
    hyphens: auto;
  }
  .letter-body p { margin-bottom: 18px; }
  .closing {
    position: absolute;
    top: 712px;
    left: 77px;
    font-family: "Questrial", sans-serif;
    font-size: 12px;
    color: var(--body-text);
  }
  .signature {
    position: absolute;
    top: 780px;
    left: 74px;
    width: 150px;
    height: 60px;
    background: linear-gradient(90deg, var(--signature-tone), #dde5f3);
    border-radius: 4px;
  }
  .contact-footer {
    position: absolute;
    top: 1038px;
    left: 0;
    width: 100%;
    font-family: "Roboto", sans-serif;
    font-size: 11.5px;
    line-height: 14px;
    color: var(--footer-text);
  }
  .contact-column { position: absolute; top: 0; }
  .contact-column.address { left: 80px; }
  .contact-column.phones { left: 346px; }
  .contact-column.online { left: 616px; }
  .contact-line { display: flex; align-items: center; gap: 6px; height: 14px; }
  .contact-line svg { width: 10px; height: 10px; fill: var(--navy); flex-shrink: 0; }
  .footer-band {
    position: absolute;
    left: 0;
    bottom: 0;
    width: 800px;
    height: 20px;
    background: var(--navy);
  }
</style>
</head>
<body>
  <main class="letterhead">
    <div class="brand-name">KORVEN</div>

    <p class="salutation">Dear Mr. Harlow,</p>

    <div class="letter-body">
      <p>Lorem ipsum dolor sit amet, consectetur adipiscing elit. Donec orci purus, luctus vitae dignissim eu, iaculis sed purus. Vivamus faucibus, ipsum nec aliquet viverra, leo mauris condimentum ligula, sit amet sagittis enim ligula quis arcu. Nam egestas tortor id nisi porttitor mattis. In tortor ante, ultricies in suscipit a, tempus non massa. Vivamus et auctor mi. Fusce vel massa nulla. Phasellus nec eros mauris, et scelerisque orci.</p>
      <p>Donec malesuada orci vitae nulla accumsan porta a id massa. Quisque accumsan iaculis magna sit amet fringilla. Maecenas consequat, magna eget tincidunt semper, odio nibh rutrum mi, id feugiat ante nisi eu risus. Vestibulum nunc orci, rhoncus a placerat in, ultricies in mi. Cras mattis varius eros, vel fringilla nisi suscipit eget. Quisque scelerisque sagittis nulla at porttitor.</p>
      <p>Sed id augue vitae urna euismod commodo aliquet a quam. Pellentesque arcu velit, cursus et malesuada ut, consequat et diam. Nullam erat sem, rhoncus id ullamcorper vitae, rhoncus et arcu. In ultricies ultricies nulla, ut rutrum nisi iaculis at. Donec eu magna a metus ornare faucibus. Fusce aliquet faucibus ultricies. Morbi semper, est id tincidunt gravida, sem arcu adipiscing lacus, ac bibendum nulla leo eu purus. Quisque nec diam sed risus consectetur a ccumsan quis quis nibh. Vestibulum id purus lorem.</p>
      <p>It is a long established fact that a reader will be distracted by the readable content of a page when looking at its layout. The point of using Lorem Ipsum is that it has a more-or-less normal distribution of letters, as opposed to using 'Content here, content here', making it look like readable English. Many desktop publishing packages</p>
    </div>

    <p class="closing">Sincerely,</p>
    <div class="signature" role="img" aria-label="Handwritten signature of Daniel Harlow in blue ink"></div>

    <footer class="contact-footer">
      <div class="contact-column address">
        <div class="contact-line">PO Box 417</div>
        <div class="contact-line">Lindale, OR 97390</div>
      </div>
      <div class="contact-column phones">
        <div class="contact-line">
          <svg viewBox="0 0 10 10" aria-hidden="true"><path d="M2 0.5 L3.6 0.5 L4.2 2.8 L3 3.6 C3.6 5 5 6.4 6.4 7 L7.2 5.8 L9.5 6.4 L9.5 8 C9.5 9 8.8 9.5 8 9.5 C4 9.2 0.8 6 0.5 2 C0.5 1.2 1 0.5 2 0.5 Z"/></svg>
          (555) 201-7734
        </div>
        <div class="contact-line">
          <svg viewBox="0 0 10 10" aria-hidden="true"><rect x="2.5" y="0.5" width="5" height="3"/><rect x="0.5" y="4" width="9" height="4" rx="1"/><rect x="2.5" y="8.5" width="5" height="1.2"/></svg>
          (555) 201-7790
        </div>
      </div>
      <div class="contact-column online">
        <div class="contact-line">
          <svg viewBox="0 0 10 10" aria-hidden="true"><rect x="0.5" y="2" width="9" height="6.5"/><path d="M0.5 2 L5 5.6 L9.5 2" fill="none" stroke="#f0f0f1" stroke-width="0.9"/></svg>
          hello@korvenwp.com
        </div>
        <div class="contact-line">
          <svg viewBox="0 0 10 10" aria-hidden="true"><circle cx="5" cy="5" r="4.5"/><path d="M5 0.8 C3.4 3 3.4 7 5 9.2 M5 0.8 C6.6 3 6.6 7 5 9.2 M0.8 5 H9.2" fill="none" stroke="#f0f0f1" stroke-width="0.7"/></svg>
          www.korvenwp.com
        </div>
      </div>
    </footer>

    <div class="footer-band" aria-hidden="true"></div>
  </main>
</body>
</html>
```